Recruiting ad for Caregivers and Nurses

We need a few amazing, fun, catchy, creative recruiting ads for Caregivers and Nurses to care for homecare patients on the island of Oahu, in Hawaii. We are an in home care company called Brantley Homecare. Our care services are provided 24/7, so we need staff that can work days, nights, weekdays, weekends. We need catchy fun ads to entice caregivers and nurses to call our office to inquire about jobs available. Our patients age range is from babies to seniors. We need caregivers and nurses for basic patient care (bathing, dressing, ambulating, preparing meals, medication reminders, light housekeeping) and complex patients (oxygen, tube feeding, injections, vents, wound care). Here are some bullets to consider including:
*Full-time and Part-time Positions Available (days, nights, weekdays, weekends)
*Sign-On Bonus Programs Offered up to $500
*Refer a Friend Bonus Program
*Holiday Pay
*2 Health Plans to Choose from
*Island-Wide Locations
*All PPE Provided (masks, gloves, etc)
*401K Program
*Tuition Benefits

```html
<!DOCTYPE html>
<html lang="en">
<head>
<meta charset="utf-8">
<title>Brantley Homecare – We're Hiring</title>
<link rel="stylesheet" href="https://fonts.googleapis.com/css2?family=Cinzel:wght@400;600;700&family=Crimson+Text:ital,wght@0,400;0,600;0,700;1,400&display=swap">
<style>
  :root{
    --teal:#3fc3cf;
    --teal-deep:#1fa3ad;
    --teal-dark:#0f7f87;
    --teal-pale:#bfeef1;
    --coral:#f07c4a;
    --ink:#2b2b2b;
    --night:#1c1c1d;
    --paper:#f8f8f6;
    --stage:#eef0f2;
    --white:#ffffff;
  }
  *{margin:0;padding:0;box-sizing:border-box}
  html,body{width:1200px;height:1077px;overflow:hidden}
  body{background:var(--stage);font-family:"Crimson Text",Georgia,serif;color:var(--ink)}

  .flyer{position:absolute;left:200px;top:20px;width:800px;height:1037px;overflow:hidden;
    background:var(--paper);box-shadow:0 6px 24px rgba(0,0,0,.18)}

  .hero{position:absolute;left:0;top:0;width:800px;height:570px;
    background:linear-gradient(180deg,var(--teal-pale) 0%,var(--teal) 55%,var(--teal-deep) 100%)}
  .hero-photo{position:absolute;left:220px;top:0;width:580px;height:380px;
    background:radial-gradient(ellipse at 55% 40%,rgba(255,255,255,.85) 0%,rgba(200,236,240,.7) 45%,rgba(63,195,207,0) 80%)}

  .brand-box{position:absolute;left:40px;top:200px;width:200px;height:150px;background:var(--white);
    display:flex;flex-direction:column;align-items:center;justify-content:center;gap:12px;
    box-shadow:0 2px 8px rgba(0,0,0,.12)}
  .brand-box .brand-square{width:44px;height:44px;background:var(--coral)}
  .brand-box .brand-name{font-family:"Crimson Text",Georgia,serif;font-weight:600;font-size:26px;
    color:var(--teal-dark);text-align:center;line-height:1}

  .headline-small{position:absolute;left:70px;top:365px;font-family:"Cinzel",serif;font-weight:700;
    font-size:54px;color:var(--white);letter-spacing:1px;line-height:1}
  .headline-big{position:absolute;left:60px;top:400px;font-family:"Cinzel",serif;font-weight:700;
    font-size:148px;color:var(--white);letter-spacing:2px;line-height:1}

  .positions-band{position:absolute;left:0;top:570px;width:800px;height:48px;background:var(--teal-deep);
    color:var(--white);font-size:28px;text-align:center;line-height:48px;letter-spacing:.5px}

  .benefits{position:absolute;left:0;top:618px;width:800px;height:250px;
    background:linear-gradient(180deg,#fbfbfa 0%,#eef3f3 100%)}
  .benefits-title{position:absolute;left:0;top:16px;width:100%;text-align:center;
    font-family:"Cinzel",serif;font-size:20px;letter-spacing:10px;color:var(--ink)}
  .benefit-grid{position:absolute;left:40px;top:58px;width:740px;display:grid;
    grid-template-columns:repeat(3,1fr);grid-auto-rows:60px;column-gap:20px}
  .benefit{display:flex;align-items:center;gap:12px;font-size:17px;line-height:1.05}
  .benefit svg{flex:0 0 44px;width:44px;height:44px;stroke:var(--coral);fill:none;stroke-width:2;
    stroke-linecap:round;stroke-linejoin:round}

  .contact{position:absolute;left:0;top:868px;width:800px;height:169px;background:var(--night);color:var(--white)}
  .contact-title{position:absolute;left:40px;top:18px;font-size:26px;letter-spacing:.5px}
  .contact-title .accent{color:var(--coral);font-weight:700}
  .contact-rule{position:absolute;left:40px;top:58px;width:720px;height:1px;background:var(--coral)}
  .contact-direct{position:absolute;left:40px;top:72px}
  .contact-line{display:flex;align-items:center;gap:10px}
  .contact-phone{font-size:36px;font-weight:700}
  .contact-web{font-size:24px;margin-top:4px}
  .contact-line svg{width:22px;height:22px;fill:var(--teal)}
  .contact-divider{position:absolute;left:410px;top:76px;width:1px;height:78px;background:var(--teal)}
  .contact-address{position:absolute;left:436px;top:82px;display:flex;gap:10px;font-size:21px;line-height:1.25}
  .contact-address svg{width:20px;height:26px;fill:var(--teal);flex:0 0 20px}
</style>
</head>
<body>
<main class="flyer">
  <section class="hero">
    <div class="hero-photo" role="img" aria-label="Photo of three smiling healthcare workers in white coats and scrubs"></div>
    <div class="brand-box">
      <span class="brand-square"></span>
      <span class="brand-name">Brantley Homecare</span>
    </div>
    <h2 class="headline-small">WE'RE</h2>
    <h1 class="headline-big">HIRING</h1>
  </section>

  <div class="positions-band">Full-time and Part-time Positions Available</div>

  <section class="benefits">
    <h3 class="benefits-title">WHY WORK WITH US</h3>
    <div class="benefit-grid">
      <div class="benefit">
        <svg viewBox="0 0 44 44"><circle cx="22" cy="18" r="13"/><path d="M14 29l-4 11 7-3 3 5 2-9M30 29l4 11-7-3-3 5"/></svg>
        <span>Sign-On Bonus Programs Offered up to <b>$500</b></span>
      </div>
      <div class="benefit">
        <svg viewBox="0 0 44 44"><circle cx="16" cy="14" r="8"/><path d="M16 22v18M26 34c4 0 8-3 9-8M31 24l4 2 2-4"/></svg>
        <span>Refer a Friend Bonus Program</span>
      </div>
      <div class="benefit">
        <svg viewBox="0 0 44 44"><rect x="6" y="10" width="32" height="28" rx="2"/><path d="M6 18h32M14 6v8M30 6v8M14 26h16M14 31h10"/></svg>
        <span>Holiday Pay</span>
      </div>
      <div class="benefit">
        <svg viewBox="0 0 44 44"><rect x="9" y="6" width="26" height="34" rx="2"/><path d="M16 6v4h12V6M15 18h14M15 24h14M15 30h9"/></svg>
        <span>2 Health Plans to Choose from</span>
      </div>
      <div class="benefit">
        <svg viewBox="0 0 44 44"><path d="M4 38c8-6 28-6 36 0M22 34V16M22 16c-4-5-10-5-14-2M22 16c4-5 10-5 14-2M22 16c-2-4-2-8 0-10"/></svg>
        <span>Island-Wide Locations</span>
      </div>
      <div class="benefit">
        <svg viewBox="0 0 44 44"><circle cx="22" cy="16" r="9"/><path d="M22 11v10M19 13h5a2 2 0 0 1 0 4h-4a2 2 0 0 0 0 4h5M6 30h10l6 4h10M6 38h26l8-8"/></svg>
        <span>401K Program</span>
      </div>
      <div class="benefit">
        <svg viewBox="0 0 44 44"><path d="M12 18v10c0 4 20 4 20 0V18M22 30v0"/><rect x="10" y="16" width="24" height="12" rx="6"/><path d="M14 22h16"/></svg>
        <span>All PPE Provided (masks, gloves, etc)</span>
      </div>
      <div class="benefit">
        <svg viewBox="0 0 44 44"><path d="M4 16l18-8 18 8-18 8zM12 20v9c6 5 14 5 20 0v-9M40 16v12"/></svg>
        <span>Tuition Benefits</span>
      </div>
    </div>
  </section>

  <footer class="contact">
    <p class="contact-title">NEED MORE INFORMATION? <span class="accent">CONTACT US</span></p>
    <div class="contact-rule"></div>
    <div class="contact-direct">
      <div class="contact-line contact-phone">
        <svg viewBox="0 0 24 24"><path d="M6.6 10.8a15 15 0 0 0 6.6 6.6l2.2-2.2a1 1 0 0 1 1-.25 11.4 11.4 0 0 0 3.6.57 1 1 0 0 1 1 1V20a1 1 0 0 1-1 1A17 17 0 0 1 3 4a1 1 0 0 1 1-1h3.5a1 1 0 0 1 1 1c0 1.25.2 2.45.57 3.57a1 1 0 0 1-.25 1z"/></svg>
        <span>808-555-0142</span>
      </div>
      <div class="contact-line contact-web">
        <svg viewBox="0 0 24 24"><path d="M12 2a10 10 0 1 0 0 20 10 10 0 0 0 0-20zm6.9 6h-3a15 15 0 0 0-1.3-3.9A8 8 0 0 1 18.9 8zM12 4c.8 1.2 1.5 2.5 1.9 4h-3.8c.4-1.5 1.1-2.8 1.9-4zM4.3 14a8 8 0 0 1 0-4h3.4a16 16 0 0 0 0 4zm.8 2h3a15 15 0 0 0 1.3 3.9A8 8 0 0 1 5.1 16zm3-8h-3a8 8 0 0 1 4.3-3.9A15 15 0 0 0 8.1 8zM12 20c-.8-1.2-1.5-2.5-1.9-4h3.8c-.4 1.5-1.1 2.8-1.9 4zm2.3-6H9.7a14 14 0 0 1 0-4h4.6a14 14 0 0 1 0 4zm.3 5.9a15 15 0 0 0 1.3-3.9h3a8 8 0 0 1-4.3 3.9zm1.7-5.9a16 16 0 0 0 0-4h3.4a8 8 0 0 1 0 4z"/></svg>
        <span>www.brantleycare.com</span>
      </div>
    </div>
    <div class="contact-divider"></div>
    <address class="contact-address">
      <svg viewBox="0 0 20 26"><path d="M10 0a10 10 0 0 0-10 10c0 7.5 10 16 10 16s10-8.5 10-16A10 10 0 0 0 10 0zm0 14a4 4 0 1 1 0-8 4 4 0 0 1 0 8z"/></svg>
      <span>4870 Lanakila Ave. Suite 210<br>Honolulu, HI 96817</span>
    </address>
  </footer>
</main>
</body>
</html>
```